Singapore Restaurant Menu Design

We need a menu designed for our new Singapore inspire restaurant located here in New Plymouth New Zealand. More Information in attached documents.
Updates

Sick

Target Market(s)

New Zealanders

Colors

Designer to choose only greyscale colors for use in the design.

Requirements
Nice to have
• Images of Singapore food however we do not want this to distract from the overall menu design as we still want the menu to be super clean

```html
<!DOCTYPE html>
<html lang="en">
<head>
<meta charset="utf-8">
<title>Menu – Noodles &amp; Rice</title>
<link rel="stylesheet" href="https://fonts.googleapis.com/css2?family=Arimo:ital,wght@0,400;0,700;1,400&display=swap">
<style>
  :root {
    --paper-light: #fafafa;
    --paper-mid: #efefef;
    --paper-edge: #d9d9d9;
    --ink: #1c1c1c;
    --ink-soft: #2b2b2b;
    --swirl: #cfcfcf;
  }
  * { margin: 0; padding: 0; box-sizing: border-box; }
  html, body { width: 849px; height: 1200px; overflow: hidden; }
  body {
    font-family: "Arimo", Arial, sans-serif;
    color: var(--ink);
  }
  .menu-page {
    position: relative;
    width: 849px;
    height: 1200px;
    background: radial-gradient(ellipse 75% 65% at 45% 45%, var(--paper-light) 0%, var(--paper-mid) 65%, var(--paper-edge) 100%);
    overflow: hidden;
  }
  .corner-flourish {
    position: absolute;
    left: -30px;
    bottom: -20px;
    width: 300px;
    height: 230px;
    border-radius: 50%;
    background: radial-gradient(ellipse at 40% 60%, var(--swirl) 0%, rgba(207,207,207,0.5) 40%, rgba(207,207,207,0) 72%);
  }
  .dish {
    position: absolute;
    left: 57px;
    width: 770px;
  }
  .dish-line {
    display: flex;
    align-items: baseline;
    font-weight: 700;
    font-size: 26px;
    line-height: 32px;
  }
  .dish-name { white-space: nowrap; }
  .leader {
    flex: 1;
    margin: 0 22px 0 6px;
    height: 4px;
    background-image: radial-gradient(circle, var(--ink) 1.5px, transparent 1.8px);
    background-size: 9px 4px;
    background-repeat: repeat-x;
  }
  .dish-price { white-space: nowrap; font-size: 22px; }
  .dish-desc {
    margin-top: 33px;
    width: 716px;
    font-style: italic;
    font-size: 19px;
    line-height: 29px;
    color: var(--ink-soft);
  }
  .dish-desc.justified { text-align: justify; text-align-last: left; }
  .section-title {
    position: absolute;
    top: 380px;
    left: 0;
    width: 849px;
    text-align: center;
    font-size: 40px;
    line-height: 48px;
    font-weight: 700;
    text-decoration: underline;
    text-underline-offset: 6px;
    text-decoration-thickness: 3px;
  }
  .group-title {
    position: absolute;
    left: 57px;
    top: 482px;
    font-size: 26px;
    line-height: 32px;
    font-weight: 700;
  }
  .group-title .note { font-size: 18px; font-weight: 400; }
</style>
</head>
<body>
<main class="menu-page">
  <div class="corner-flourish" role="img" aria-label="Faint decorative swirl in the lower left corner"></div>

  <section class="dish" style="top:21px">
    <div class="dish-line"><span class="dish-name">Laksa Ala Katong Singapore</span><span class="leader"></span><span class="dish-price">$18.00</span></div>
    <p class="dish-desc">A Peranakan style prawn based broth noodles with prawns, squid and<br>mussels topped with boiled egg &amp; fried tofu cubes.</p>
  </section>

  <section class="dish" style="top:171px">
    <div class="dish-line"><span class="dish-name">Hor Fun Noodles</span><span class="leader"></span><span class="dish-price">$16.00</span></div>
    <p class="dish-desc">Flat rice noodles stir fried with dark sweet soy sauce and a choice of<br>seafood or pork in a silky egg gravy.</p>
  </section>

  <h2 class="section-title">Rice</h2>

  <h3 class="group-title">Singapore Chicken rice <span class="note">(Family style sharing)</span></h3>

  <section class="dish" style="top:573px">
    <div class="dish-line"><span class="dish-name">Half chicken for 2 pax</span><span class="leader"></span><span class="dish-price">$20.00</span></div>
  </section>

  <section class="dish" style="top:672px">
    <div class="dish-line"><span class="dish-name">Whole chicken for 4 pax</span><span class="leader"></span><span class="dish-price">$35.00</span></div>
    <p class="dish-desc justified">The Singapore classic - aromatic roasted chicken with fragrant rice cooked in a chicken broth accompanied by seasonal veg in oyster sauce and ginger sweet chili dip.</p>
  </section>

  <section class="dish" style="top:850px">
    <div class="dish-line"><span class="dish-name">Nasi Lemak 2 pax</span><span class="leader"></span><span class="dish-price">$18.00</span></div>
    <p class="dish-desc justified">Jasmine rice cooked in coconut cream infused in pandan leaves, comes with condiments of fried egg, ikan bilis, toasted nuts, crispy fried chicken and shrimp based sambal.</p>
  </section>

  <section class="dish" style="top:1045px">
    <div class="dish-line"><span class="dish-name">Fried Rice</span><span class="leader"></span><span class="dish-price">$18.00</span></div>
    <p class="dish-desc">Chinese style fried rice with choice of chicken, beef or veg in sesame<br>oil &amp; fish sauce.</p>
  </section>
</main>
</body>
</html>
```